Cool business cards

Use my existing logo from sketch harbor (see images I have uploaded) and design a really cool non-stuffy business card. I am a divorce mediator.

```html
<!DOCTYPE html>
<html lang="en">
<head>
<meta charset="UTF-8">
<title>Sketch Harbor – Business Card</title>
<link rel="stylesheet" href="https://fonts.googleapis.com/css2?family=Roboto:wght@400;500&family=Saira+Semi+Condensed:wght@600&display=swap">
<style>
  :root {
    --backdrop: #c4c4c4;
    --card-white: #f4f4f2;
    --teal: #35a7b5;
    --teal-deep: #2e97a4;
    --forest: #3a8469;
    --forest-text: #2f7d5c;
    --ink: #2a2a2a;
    --paper-ink: #ffffff;
  }
  * { margin: 0; padding: 0; box-sizing: border-box; }
  html, body {
    width: 1200px; height: 576px; overflow: hidden;
    background: var(--backdrop);
    font-family: "Roboto", Arial, sans-serif;
  }
  .stage { position: relative; width: 1200px; height: 576px; }

  .card {
    position: absolute; top: 139px;
    width: 484px; height: 292px;
    border-radius: 14px; overflow: hidden;
  }

  /* Front */
  .card-front {
    left: 82px;
    background: linear-gradient(60deg, var(--teal-deep) 0%, #3c9483 45%, var(--forest) 100%);
    color: var(--paper-ink);
    text-align: center;
  }
  .front-brand {
    position: absolute; left: 0; right: 0; top: 110px;
    font-size: 34px; font-weight: 400; letter-spacing: 0.5px; line-height: 1;
  }
  .front-tagline {
    position: absolute; left: 0; right: 0; top: 169px;
    display: flex; align-items: center; justify-content: center; gap: 8px;
    font-size: 13.5px; letter-spacing: 0.4px; line-height: 1;
  }
  .rule { display: block; }

  /* Back */
  .card-back { left: 602px; width: 481px; height: 290px; background: var(--card-white); }
  .back-rings { position: absolute; inset: 0; }
  .back-brand {
    position: absolute; left: 26px; top: 36px;
    font-size: 24px; line-height: 1; color: var(--forest-text); font-weight: 400;
  }
  .back-tagline {
    position: absolute; left: 24px; top: 70px;
    display: flex; align-items: center; gap: 6px;
    font-size: 9.5px; line-height: 1; letter-spacing: 0.3px; color: var(--teal);
  }
  .side-tab {
    position: absolute; left: -16px; top: 126px;
    width: 32px; height: 32px; border-radius: 50%; background: var(--forest);
  }
  .person-name {
    position: absolute; left: 23px; top: 128px;
    font-family: "Saira Semi Condensed", "Roboto", sans-serif;
    font-weight: 600; font-size: 19px; line-height: 1; color: var(--forest-text);
  }
  .person-role {
    position: absolute; left: 23px; top: 152px;
    font-size: 12px; line-height: 1; color: var(--ink);
  }
  .contact-list {
    position: absolute; left: 23px; top: 197px; list-style: none;
    font-size: 12.5px; color: var(--ink);
  }
  .contact-list li { display: flex; align-items: center; gap: 10px; height: 18.5px; }
  .contact-list svg { width: 11px; height: 11px; fill: var(--forest); }
  .postal-address {
    position: absolute; left: 26px; top: 260px;
    font-size: 12.5px; line-height: 1; color: var(--ink);
  }
</style>
</head>
<body>
<main class="stage">

  <section class="card card-front" aria-label="Card front">
    <div class="front-brand">Sketch Harbor</div>
    <div class="front-tagline">
      <svg class="rule" width="50" height="4" viewBox="0 0 50 4"><polygon points="0,2 50,0 50,4" fill="#fff"/></svg>
      <span>I AM A DIVORCE MEDIATOR</span>
      <svg class="rule" width="50" height="4" viewBox="0 0 50 4"><polygon points="0,0 50,2 0,4" fill="#fff"/></svg>
    </div>
  </section>

  <section class="card card-back" aria-label="Card back">
    <svg class="back-rings" width="481" height="290" viewBox="0 0 481 290">
      <circle cx="458" cy="145" r="176" fill="none" stroke="var(--forest)" stroke-width="28"/>
      <circle cx="458" cy="145" r="97" fill="none" stroke="var(--teal)" stroke-width="27"/>
    </svg>

    <div class="back-brand">Sketch Harbor</div>
    <div class="back-tagline">
      <svg width="40" height="3" viewBox="0 0 40 3"><polygon points="0,1.5 40,0 40,3" fill="var(--forest)"/></svg>
      <span>I AM A DIVORCE MEDIATOR</span>
      <svg width="40" height="3" viewBox="0 0 40 3"><polygon points="0,0 40,1.5 0,3" fill="var(--forest)"/></svg>
    </div>

    <span class="side-tab"></span>
    <div class="person-name">Mara Linwood</div>
    <div class="person-role">Managing Director</div>

    <ul class="contact-list">
      <li>
        <svg viewBox="0 0 12 12"><path d="M1 3c0-1 1-2 5-2s5 1 5 2v1H8V3H4v1H1z M3 5h6l2 6H1z"/></svg>
        <span>555-014-2290</span>
      </li>
      <li>
        <svg viewBox="0 0 12 12"><path d="M0 2h12v8H0z" /><path d="M0 2l6 5 6-5" stroke="#f4f4f2" stroke-width="1" fill="none"/></svg>
        <span>mara@sketchharbor.com</span>
      </li>
      <li>
        <svg viewBox="0 0 12 12"><circle cx="6" cy="6" r="5.5"/><path d="M0.5 6h11M6 0.5v11M2 3h8M2 9h8" stroke="#f4f4f2" stroke-width="0.8"/></svg>
        <span>www.sketchharbor.com</span>
      </li>
    </ul>
    <div class="postal-address">48 Quayside Lane, Fairport, US 104501</div>
  </section>

</main>
</body>
</html>
```